Amber Tides: Lantern Tales from Seven Winters by the Northern Sea and Other Small Wonders

Good day! I am excited to work again with you, amazing designers! This time I am looking for the cover design of my book.
Dimensions 6” x 9”
The book name is as my name project. I love simplicity, but yet that is impactful. I love colours, I don't have a specific colour in mind, but I like the mustard colour as the one in the logo of my company. I am open to ideas! I have attached some cover samples that I like so that it gives a better idea of what I have on mind.
I am looking for something that looks professional, yet, not super serious, that it's approachable to people. Something that calls their attention at first glance.
I am working with my editor and my interior designer as well to finalize this part of the book. I will be working with the person that I select for the book design to finalize it.
About the book, here a passage of an unedited version of the introduction for guidance :
My intention is to take you on a journey to help you to understand what is going on in your mind so that you get out from anything that is holding you back in your life. My intention is to guide you to start fully living and experiencing a life that your mind even have yet conceived. To experience a life where you live fearless and without suffering. Living your life where you are the navigator and the creator of how you are experiencing it and you are living in a world of possibilities where there are no limitations.
For it, we will start to understand more about the mind and about the brain. I am not a neuroscientist and neither I consider my self an expert in the workings of the brain, what I know is the result of my fascination about our brain. This curiosity and the part of me that likes to understand how things work took me to read, research and learn about how our brain works and how its intrinsic mechanisms are subconsciously influencing and limiting us. I encourage you to stay on this part, it can be a bit technical, but understanding how it works will empower you not to allow your mind to dictate the way you approach your life and to live on autopilot.
We will continue to describe how you have been programmed throughout your life, putting you inside a box limited by your subconscious beliefs and ideas about the world. In this part, we will also discuss what ego is, how it is subconsciously limiting you and how the ways of when ego manifests itself are limiting you and making you suffer. Now that you know how you have been enclosed in your mind for all your life, we will move to discuss how you can get out of it. You will learn how to master your emotions to eliminate your suffering and not allow them to control the direction of your life and use them as a mechanism to get out from your programed mind. We continue to discuss how to leverage the power of your mind and harness your power of choice. Finally, I invite you to see yourself as a holistic being so that you start truly living and take control over the direction of your life, by nourishing and taking care of all those aspects of you utilizing their wisdom and synergy to achieve higher connection within yourself, your soul and live your life in a higher level of consciousness with peace, flow, love and purpose.

```html
<!DOCTYPE html>
<html lang="en">
<head>
<meta charset="utf-8">
<title>Amber Tides — Book Cover</title>
<link href="https://fonts.googleapis.com/css2?family=Archivo+Black&family=Jost:wght@400&family=Cormorant+Garamond:wght@500&display=swap" rel="stylesheet">
<style>
  :root {
    --backdrop: #949494;
    --sky-dusk: #6c6878;
    --sky-haze: #9a8d96;
    --sky-warm: #d8a468;
    --sun-glow: #ffd778;
    --sun-core: #fff4cc;
    --horizon: #b9763a;
    --field-light: #7a4b24;
    --field-dark: #2f1d10;
    --ink-light: #ffffff;
    --ink-soft: #f6efe6;
  }
  * { margin: 0; padding: 0; box-sizing: border-box; }
  html, body {
    width: 1200px;
    height: 800px;
    overflow: hidden;
    background: var(--backdrop);
  }
  .canvas {
    position: relative;
    width: 1200px;
    height: 800px;
    display: flex;
    align-items: center;
    justify-content: center;
  }
  .book-cover {
    position: relative;
    width: 480px;
    height: 720px;
    overflow: hidden;
    box-shadow: 0 10px 30px rgba(0,0,0,0.25);
  }
  .cover-scene {
    position: absolute;
    inset: 0;
    background:
      radial-gradient(ellipse 38% 22% at 96% 64%, var(--sun-core) 0%, var(--sun-glow) 30%, rgba(255,200,100,0) 100%),
      radial-gradient(ellipse 70% 30% at 85% 60%, rgba(240,170,70,0.75) 0%, rgba(240,170,70,0) 100%),
      linear-gradient(180deg,
        var(--sky-dusk) 0%,
        #7a7280 22%,
        var(--sky-haze) 38%,
        #c3a48a 50%,
        var(--sky-warm) 58%,
        #e8b25a 63%,
        var(--horizon) 65.5%,
        var(--field-light) 70%,
        #5a3519 82%,
        var(--field-dark) 100%);
  }
  .cover-title {
    position: absolute;
    top: 19%;
    left: 0;
    right: 0;
    text-align: center;
    font-family: "Archivo Black", "Arial Black", sans-serif;
    font-size: 62px;
    line-height: 1;
    letter-spacing: 0.5px;
    color: var(--ink-light);
    text-transform: uppercase;
  }
  .cover-subtitle {
    position: absolute;
    top: 69%;
    left: 0;
    right: 0;
    text-align: center;
    font-family: "Jost", "Futura", sans-serif;
    font-size: 17px;
    line-height: 1.35;
    letter-spacing: 2px;
    color: var(--ink-soft);
    text-transform: uppercase;
  }
  .cover-author {
    position: absolute;
    bottom: 3.5%;
    left: 0;
    right: 0;
    text-align: center;
    font-family: "Cormorant Garamond", "Times New Roman", serif;
    font-weight: 500;
    font-size: 34px;
    letter-spacing: 7px;
    color: var(--ink-light);
    text-transform: uppercase;
  }
</style>
</head>
<body>
  <main class="canvas">
    <article class="book-cover">
      <div class="cover-scene" role="img" aria-label="Photograph of a long-haired woman seen from behind standing in a wheat field at golden sunset under a cloudy sky"></div>
      <h1 class="cover-title">Amber Tides</h1>
      <p class="cover-subtitle">Lantern Tales from Seven Winters<br>by the Northern Sea<br>and Other Small Wonders</p>
      <p class="cover-author">Author Name</p>
    </article>
  </main>
</body>
</html>
```